Stationary design for real estate company in Trinidad and Tobago

Kestra Realty Ltd. , real estate company operating in Trinidad and Tobago, requires a sleek, modern and professional stationary package to wow our customers and potential new clients. we want to look sleek and professional; first impressions count in this business!
Business Address:
Level 1, Marlowe Point Tower
4C Seldon Grove Boulevard
Marlowe Point
Colwyn Pereira Highway
Port of Spain
Trinidad
Tel: + 1 868 555 0147
www.kestra-tt.com
info@kestra-tt.com

```html
<!DOCTYPE html>
<html lang="en">
<head>
<meta charset="utf-8">
<title>Kestra Realty – Business Card</title>
<link rel="stylesheet" href="https://fonts.googleapis.com/css2?family=Open+Sans:wght@400;700&display=swap">
<style>
  :root {
    --navy: #17325f;
    --gold: #c9ae6f;
    --ink: #2b2b2b;
    --paper: #ffffff;
    --backdrop: #d6d6d6;
  }
  * { box-sizing: border-box; margin: 0; padding: 0; }
  html, body {
    width: 1200px; height: 896px; overflow: hidden;
    background: var(--backdrop);
    font-family: "Open Sans", Arial, sans-serif;
  }
  .card {
    position: absolute; left: 334px;
    width: 528px; height: 301px;
    background: var(--paper);
    border-radius: 24px;
    overflow: hidden;
    box-shadow: 0 10px 18px rgba(0,0,0,0.22);
  }
  .card--front { top: 125px; }
  .card--back { top: 475px; }

  .brand {
    position: absolute;
    display: flex; align-items: center;
    color: var(--navy);
    font-weight: 700;
    white-space: nowrap;
  }
  .brand__dot { border-radius: 50%; background: var(--gold); flex: none; }
  .card--front .brand { left: 40px; top: 132px; font-size: 24px; gap: 9px; letter-spacing: 0.5px; }
  .card--front .brand__dot { width: 22px; height: 22px; }
  .card--back .brand { left: 0; right: 0; top: 128px; justify-content: center; font-size: 50px; gap: 18px; letter-spacing: 1px; }
  .card--back .brand__dot { width: 42px; height: 42px; }

  .divider {
    position: absolute; left: 273px; top: 55px;
    width: 2px; height: 192px; background: var(--navy);
  }
  .details { position: absolute; left: 288px; top: 50px; color: var(--ink); }
  .details__name { color: var(--navy); font-weight: 700; font-size: 21px; line-height: 26px; padding-left: 2px; }
  .details__role { font-size: 14.5px; line-height: 19px; padding-left: 3px; }
  .contact { list-style: none; margin-top: 14px; font-size: 14.5px; line-height: 19px; }
  .contact li { display: flex; align-items: center; gap: 5px; }
  .contact svg { width: 12px; height: 12px; fill: var(--navy); flex: none; }
  .address { margin-top: 11px; font-size: 14.5px; line-height: 18.7px; font-style: normal; }

  .band { position: absolute; left: 0; bottom: 0; width: 528px; height: 30px; }
</style>
</head>
<body>

<section class="card card--front" aria-label="Business card front">
  <div class="brand"><span class="brand__dot"></span>KESTRA REALTY</div>
  <div class="divider"></div>
  <div class="details">
    <p class="details__name">DANIEL OKORO</p>
    <p class="details__role">Managing Director</p>
    <ul class="contact">
      <li><svg viewBox="0 0 12 12"><path d="M1 4.5C1 3 3 2 6 2s5 1 5 2.5V5H8.5V4h-5v1H1z M2.5 6h7l1 4h-9z"/></svg>+ 1 868 555 0147</li>
      <li><svg viewBox="0 0 12 12"><path d="M1 3h10v1L6 7 1 4z M1 5.2l5 3 5-3V10H1z"/></svg>info@kestra-tt.com</li>
      <li><svg viewBox="0 0 12 12"><circle cx="6" cy="6" r="5.2"/><path d="M4 3.5l2 1-1 2 1 2-2-1z M7.5 3l1.5 1.5-1 1.5z" fill="#fff"/></svg>www.kestra-tt.com</li>
    </ul>
    <address class="address">
      Level 1, Marlowe Point Tower<br>
      4C Seldon Grove Boulevard<br>
      Marlowe Point Colwyn Pereira<br>
      Highway, Port of Spain Trinidad
    </address>
  </div>
  <svg class="band" viewBox="0 0 528 30" preserveAspectRatio="none" aria-hidden="true">
    <polygon points="0,7 283,7 278,12 0,12" fill="var(--gold)"/>
    <polygon points="0,18 272,18 264,28 0,28" fill="var(--gold)"/>
    <polygon points="295,0 528,0 528,30 268,30" fill="var(--navy)"/>
  </svg>
</section>

<section class="card card--back" aria-label="Business card back">
  <div class="brand"><span class="brand__dot"></span>KESTRA REALTY</div>
</section>

</body>
</html>
```